Website: Brightkeel Business Consultants, Qianhai SEZ, China

Our client is a business consultancy firm and will be the first to set up in the Qianhai Shenzhen-Hong Kong Modern Service Industry Cooperation Zone, China So we need a corporate website concept that engages service, finance and technology sector companies. The company can provide all the necessary services needed to set up shop in Qianhai. They are looking for a modern, international, reliable and strong image.

Here are some websites for reference prupose:

http://www.vornamesh.com/ (we like the dynamic banner and clear, clean layout of this website)

http://www.plendaradvisory.com/ (we like the background city image, use of light font, hover over menu functions and color scheme - purple and grey)

http://www.quolb.com/ (we like the simplicity of this website, clear lines and we like the dynamic banner)
Updates

Hello, We are currently undecided between three logo designs.  All three have been uploaded to the design brief so that you can use them as reference for the website design. Thx

Also please take note of the addition menu selection 'About Qianhai'. Thx

Hello all Designers, First of all we want thank you for participating in our website competition, the calibre of design was high and we appreciated the expedience. Our company is Lumenpath Web Design and Internet Marketing based in Shenzhen, China. We anticipate rapid growth in the Chinese domestic market as the country shifts in to a service sector economy. We hope to continue building reliable working relationships with you based on idea sharing and constructive feedback. Once again, Thankyou, LP Team

Target Market(s)

International finance and technology companies looking to set up in Qianhai Special Economic Zone, China

Industry/Entity Type

Finance

Requirements
Must have
• Initial design for home page and in later selection stages a secondary page will be required.

The design should be for PSD concepts only no code!

Menu bar, Photo banner -
A. Photo banner and text overlay,
B.Photo Banner and text description to left or right.

Social Connect icons, Site search bar (top right), Logo space (top left).

Menu bar at top with Home, About Us, About Qianhai, Services, Portfolio, Partners, Our Team Contact Us.

Standard 3-4 box layout - Banner at top and 2-3 boxes under banner.

Colour scheme- A. Purple and Blue, must have light background/body
B. Shades of white, black and grey.

Simple, clear, clean, sharp.

```html
<!DOCTYPE html>
<html lang="en">
<head>
<meta charset="utf-8">
<title>Brightkeel Business Consultants</title>
<link href="https://fonts.googleapis.com/css2?family=Ubuntu:wght@300;400;500&display=swap" rel="stylesheet">
<style>
:root{
  --bg:#ececec;
  --page:#ffffff;
  --purple:#86198c;
  --purple-light:#c552c8;
  --purple-dark:#8e2a9e;
  --blue:#0f9ed3;
  --blue-light:#27b6e4;
  --blue-dark:#0a84c2;
  --text:#3f3f3f;
  --icon:#4a4a4a;
}
*{margin:0;padding:0;box-sizing:border-box}
html,body{width:1194px;height:1200px;overflow:hidden;background:var(--bg);font-family:'Ubuntu',sans-serif;color:var(--text)}
.page{position:absolute;left:120px;top:0;width:960px;height:1115px;background:var(--page)}
.abs{position:absolute;white-space:nowrap}
.brand{left:146px;top:62px;display:flex;align-items:center;gap:10px;font-size:24px;font-weight:400;color:#333;letter-spacing:2px}
.brand-mark{width:16px;height:16px;border-radius:50%;background:var(--purple)}
.social{left:894px;top:75px;display:flex;gap:6px}
.social span{width:29px;height:29px;border-radius:50%;background:var(--icon)}
.search{left:824px;top:116px;width:246px;height:26px;background:#e6e6e6;border:1px solid #ddd;font-size:9px;color:#aaa;padding:7px 8px}
.search svg{position:absolute;right:7px;top:6px}
.nav{left:130px;top:151px;width:940px;height:56px;background:linear-gradient(var(--blue-light),var(--blue-dark));list-style:none}
.nav li{position:absolute;top:0;color:#fff;font-size:16px;font-weight:300;height:56px;line-height:56px;white-space:nowrap}
.nav .active{left:0;width:104px;text-align:center;background:linear-gradient(var(--purple-light),var(--purple-dark))}
.hero{left:130px;top:214px;width:940px;height:355px;background:#f4f4f4}
.hero-panel{left:136px;top:214px;width:682px;height:355px;background:linear-gradient(#e6e6e6,#f1f1f1 30%,#ececec);box-shadow:0 2px 6px rgba(0,0,0,.15)}
.hero-frame{left:152px;top:268px;width:369px;height:247px;background:#fff;box-shadow:0 1px 4px rgba(0,0,0,.2)}
.hero-photo{left:160px;top:276px;width:353px;height:230px;background:linear-gradient(120deg,#dfe6ee,#c8d4e2 50%,#b9c6d6)}
.hero-title{left:542px;top:264px;font-size:27px;color:var(--purple);line-height:38px;font-weight:400}
.hero-text{left:544px;top:343px;width:247px;font-size:10.4px;line-height:17.7px;text-align:justify;color:#555;white-space:normal}
.btn{left:705px;top:524px;width:85px;height:25px;background:var(--purple);color:#fff;font-size:11px;text-align:center;line-height:25px}
.dots{left:152px;top:540px;display:flex;gap:11px}
.dots span{width:12px;height:10px;background:#9c9c9c}
.dots span:first-child{background:var(--blue)}
.strip{top:214px;height:355px}
.h2{font-size:17px;color:var(--purple);font-weight:500}
.welcome-img{left:130px;top:627px;width:220px;height:176px;background:linear-gradient(160deg,#0d1a33,#1b3a66 55%,#7a1f24 85%,#2a2e4a)}
.body-text{font-size:10.3px;line-height:18px;text-align:justify;color:#555;white-space:normal}
.services{left:780px;top:689px;list-style:none;font-size:12.5px;color:#444}
.services li{height:26px;display:flex;align-items:center;gap:9px}
.quote{left:130px;top:859px;width:940px;height:137px;background:var(--blue);color:#fff;text-align:center}
.quote p{position:absolute;left:20px;top:34px;width:900px;font-size:12.6px;line-height:20px;white-space:normal}
.quote .mark{position:absolute;font-size:26px;font-weight:500;line-height:1}
.quote .by{position:absolute;left:0;top:103px;width:100%;font-size:16px;font-weight:500}
.partners{left:175px;top:1020px;width:850px;display:flex;justify-content:space-between;align-items:center}
.partners span{background:#d8d8d8}
.footer-nav{left:0;top:1136px;width:1194px;height:18px;font-size:12.5px;color:#333;list-style:none}
.footer-nav li{position:absolute;top:0;white-space:nowrap}
.copyright{left:0;top:1164px;width:1194px;text-align:center;font-size:12.5px;color:#333}
</style>
</head>
<body>
<div class="page"></div>

<header>
  <div class="abs brand"><span class="brand-mark"></span>Brightkeel</div>
  <div class="abs social" aria-label="Social links"><span></span><span></span><span></span><span></span><span></span></div>
  <div class="abs search">Type search
    <svg width="12" height="12" viewBox="0 0 12 12"><circle cx="5" cy="5" r="3.6" fill="none" stroke="#888" stroke-width="1.3"/><line x1="7.6" y1="7.6" x2="11" y2="11" stroke="#888" stroke-width="1.6"/></svg>
  </div>
  <ul class="abs nav">
    <li class="active">Home</li>
    <li style="left:128px">About Us</li>
    <li style="left:242px">About Qianhai</li>
    <li style="left:393px">Services</li>
    <li style="left:499px">Portfolio</li>
    <li style="left:609px">Partners</li>
    <li style="left:717px">Our Team</li>
    <li style="left:835px">Contact Us</li>
  </ul>
</header>

<section>
  <div class="abs hero"></div>
  <div class="abs hero-panel"></div>
  <div class="abs hero-frame"></div>
  <div class="abs hero-photo" role="img" aria-label="Photo of a smiling business team"></div>
  <h1 class="abs hero-title">Business Consulting<br>Company</h1>
  <p class="abs hero-text">Lorem Ipsum is simply dummy text of the printing and typesetting industry. Lorem Ipsum has been the industry's standard dummy text ever since the 1500s, when an unknown printer took a galley of type and scrambled it to make a type specimen book. Lorem Ipsum is simply dummy text of the printing and typesetting industry. Lorem Ipsum has been the industry's standard dummy text ever since the 1500s, when an unknown printer took a galley of type and scrambled .</p>
  <div class="abs btn">Read More</div>
  <div class="abs dots"><span></span><span></span><span></span><span></span></div>
  <div class="abs strip" style="left:818px;width:83px;background:linear-gradient(#d8d2cc,#b9a89a 50%,#c9b29a)" role="img" aria-label="Photo of businessmen in a meeting"></div>
  <div class="abs strip" style="left:902px;width:82px;background:linear-gradient(#3a78c2,#9cc4e6 40%,#b7d5ea 60%,#5c9a30 80%,#3f7a1e)" role="img" aria-label="Photo of a man under a blue sky on green grass"></div>
  <div class="abs strip" style="left:985px;width:85px;background:linear-gradient(#c9a58e,#e6d6c8 55%,#f4f4f4)" role="img" aria-label="Photo of a smiling businessman"></div>
</section>

<section>
  <h2 class="abs h2" style="left:130px;top:594px">Welcome to Brightkeel</h2>
  <div class="abs welcome-img" role="img" aria-label="Photo of a city skyline at night with light trails"></div>
  <p class="abs body-text" style="left:370px;top:625px;width:380px">Lorem Ipsum is simply dummy text of the printing and typesetting industry. Lorem Ipsum has been the industry's standard dummy text ever since the 1500s, when an unknown printer took a galley of type and scrambled it to make a type specimen book. It has survived not only five centuries, but also the leap into electronic typesetting, remaining essentially unchanged. It was popularised in the 1960s with the release of Letraset sheets containing Lorem Ipsum passages, and more recently with desktop .Lorem Ipsum is simply dummy text of the printing and typesetting industry. Lorem Ipsum has been the industry's standard dummy text ever ..Lorem Ipsum is simply dummy text of the printing and typesetting industry.</p>

  <h2 class="abs h2" style="left:760px;top:594px">Our Services</h2>
  <p class="abs body-text" style="left:771px;top:625px;width:300px">&nbsp;It has survived not only five centuries, but also the leap into electronic typesetting, remaining essentially unchanged. It was popularised in the 1960s .</p>
  <ul class="abs services">
    <li><svg width="6" height="9" viewBox="0 0 6 9"><path d="M1 1l3.5 3.5L1 8" fill="none" stroke="#555" stroke-width="1.2"/></svg>Voice Services</li>
    <li><svg width="6" height="9" viewBox="0 0 6 9"><path d="M1 1l3.5 3.5L1 8" fill="none" stroke="#555" stroke-width="1.2"/></svg>Non-Voice Services</li>
    <li><svg width="6" height="9" viewBox="0 0 6 9"><path d="M1 1l3.5 3.5L1 8" fill="none" stroke="#555" stroke-width="1.2"/></svg>&nbsp;IT Services</li>
    <li><svg width="6" height="9" viewBox="0 0 6 9"><path d="M1 1l3.5 3.5L1 8" fill="none" stroke="#555" stroke-width="1.2"/></svg>Applications Development Management</li>
  </ul>
</section>

<section class="abs quote">
  <span class="mark" style="left:8px;top:18px">&ldquo;</span>
  <p>Lorem ipsum dolor sit amet, consectetur adipisicing elit, sed do eiusmod tempor incididunt ut labore et dolore magna aliqua. Ut enim ad minim veniam, quis nostrud exercitation ullamco laboris nisi ut aliquip ex ea commodo consequat. Duis aute irure dolor in reprehenderit in voluptate velit esse cillum dolore eu fugiat nulla pariatur. Excepteur sint occaecat cupidatat non proident, sunt in culpa qui officia deserunt mollit anim id est laborum. <span style="font-weight:500">&rdquo;</span></p>
  <div class="by">By,Martin Caldwell</div>
</section>

<div class="abs partners" aria-label="Partner badges">
  <span style="width:92px;height:16px"></span>
  <span style="width:100px;height:30px"></span>
  <span style="width:58px;height:50px;border-radius:50%"></span>
  <span style="width:40px;height:62px"></span>
  <span style="width:62px;height:40px"></span>
  <span style="width:50px;height:50px;border-radius:50%"></span>
  <span style="width:80px;height:24px"></span>
  <span style="width:38px;height:34px"></span>
</div>

<footer>
  <ul class="abs footer-nav">
    <li style="left:229px">Home</li><li style="left:286px">|</li>
    <li style="left:308px">About Us</li><li style="left:384px">|</li>
    <li style="left:405px">About Qianhai</li><li style="left:510px">|</li>
    <li style="left:531px">Services</li><li style="left:601px">|</li>
    <li style="left:622px">Portfolio</li><li style="left:694px">|</li>
    <li style="left:715px">Partners</li><li style="left:787px">|</li>
    <li style="left:807px">Our Team</li><li style="left:887px">|</li>
    <li style="left:908px">Contact Us</li>
  </ul>
  <div class="abs copyright">Copyright@Harborline Transit.com 2011. All Rights Reserved</div>
</footer>
</body>
</html>
```